Business Card Design For Office Furniture Clearance Company

Kestrel Office Clearance - our company name pretty much explains what we do, we clear offices for high end clients, mainly plc's and large international companies.

We require a nice looking business card that displays professionalism but without being too serious.

It would be nice to see just a little more than a conventional boring business card, make sure you add some flare.

Industry/Entity Type

Office Furniture

Contact Information for Business Card

CARD 1

Tom Pardew
Director
tom@kestrelofficeclearance.co.uk
m: 07700 513928

t: 01632 419063
www.kestrelofficeclearance.co.uk

Kestrel Office Clearance
Unit K4 B
3-7 Ferndale Lane
Harwick Vale
Eastbrook
ZZ9 4QX

Office clearances at zero cost… it really is that simple.

CARD 2

Henry Walbrook
Director
henry@kestrelofficeclearance.co.uk
m: 07700 628157

t: 01632 419063

Kestrel Office Clearance
Unit K4 B
3-7 Ferndale Lane
Harwick Vale
Eastbrook
ZZ9 4QX

Font styles to use
Sans Serif

Requirements
Must have
• A white background - as we have a blue logo.
Nice to have
• Nice use of the logo - play around with this and dissect it.

```html
<!DOCTYPE html>
<html lang="en">
<head>
<meta charset="utf-8">
<title>Kestrel Office Clearance – Business Cards</title>
<link href="https://fonts.googleapis.com/css2?family=Oswald:wght@400;700&family=Arimo:wght@400&display=swap" rel="stylesheet">
<style>
  :root {
    --brand-blue: #0b63a5;
    --brand-blue-light: #0d7dc2;
    --tagline-blue: #6fb4e6;
    --paper: #ffffff;
    --ink-dark: #0b3f6b;
    --backdrop: #e8ebee;
  }
  * { box-sizing: border-box; margin: 0; padding: 0; }
  html, body { width: 1200px; height: 900px; overflow: hidden; }
  body {
    background: var(--backdrop);
    position: relative;
    font-family: "Arimo", Arial, sans-serif;
  }
  .card {
    position: absolute;
    top: 275px;
    width: 540px;
    height: 350px;
    background: var(--brand-blue);
    overflow: hidden;
    box-shadow: 0 6px 18px rgba(0,0,0,.18);
  }
  .card--front { left: 40px; }
  .card--back { left: 620px; }
  .card-shapes { position: absolute; inset: 0; }

  .front-wordmark {
    position: absolute;
    left: 362px;
    top: 112px;
    font-family: "Oswald", sans-serif;
    font-weight: 700;
    font-size: 34px;
    line-height: 40px;
    text-transform: uppercase;
    color: var(--paper);
  }
  .front-tagline {
    position: absolute;
    left: 24px;
    bottom: 16px;
    font-family: "Oswald", sans-serif;
    font-weight: 400;
    font-size: 15px;
    letter-spacing: 1.2px;
    text-transform: uppercase;
    color: var(--tagline-blue);
  }

  .contact-list {
    position: absolute;
    left: 205px;
    top: 30px;
    list-style: none;
    color: var(--paper);
    font-size: 12px;
    line-height: 19px;
  }
  .contact-list li { display: flex; align-items: center; gap: 7px; }
  .contact-icon {
    width: 12px; height: 12px;
    border-radius: 2px;
    background: var(--paper);
    color: var(--brand-blue);
    font-size: 9px;
    line-height: 12px;
    text-align: center;
    font-weight: 700;
  }
  .person {
    position: absolute;
    right: 22px;
    top: 128px;
    text-align: right;
    color: var(--paper);
  }
  .person-name { font-size: 26px; line-height: 30px; }
  .person-role { font-size: 12px; margin-top: 2px; }
  .address {
    position: absolute;
    right: 22px;
    top: 236px;
    text-align: right;
    font-style: normal;
    color: var(--ink-dark);
    font-size: 12.5px;
    line-height: 16.5px;
  }
</style>
</head>
<body>

  <section class="card card--front" aria-label="Card front">
    <svg class="card-shapes" viewBox="0 0 540 350" aria-hidden="true">
      <rect class="logo-band" x="0" y="105" width="250" height="190" fill="var(--paper)"/>
      <circle class="logo-band-end" cx="250" cy="200" r="95" fill="var(--paper)"/>
      <circle class="logo-disc" cx="250" cy="200" r="80" fill="var(--brand-blue-light)"/>
    </svg>
    <div class="front-wordmark">Kestrel<br>Office<br>Clearance</div>
    <p class="front-tagline">Office clearances at zero cost… it really is that simple.</p>
  </section>

  <section class="card card--back" aria-label="Card back">
    <svg class="card-shapes" viewBox="0 0 540 350" aria-hidden="true">
      <rect class="logo-band" x="0" y="18" width="110" height="154" fill="var(--paper)"/>
      <path class="swoosh" d="M110 95 C140 250 300 215 540 200 L540 350 L250 350 C190 300 140 220 110 95 Z" fill="var(--paper)"/>
      <circle class="logo-ring" cx="110" cy="95" r="77" fill="var(--paper)"/>
      <circle class="logo-disc" cx="110" cy="95" r="64" fill="var(--brand-blue-light)"/>
    </svg>

    <ul class="contact-list">
      <li><span class="contact-icon">m</span>07700 513928</li>
      <li><span class="contact-icon">t</span>01632 419063</li>
      <li><span class="contact-icon">@</span>tom@kestrelofficeclearance.co.uk</li>
      <li><span class="contact-icon">w</span>www.kestrelofficeclearance.co.uk</li>
    </ul>

    <div class="person">
      <p class="person-name">Tom Pardew</p>
      <p class="person-role">Director</p>
    </div>

    <address class="address">
      Kestrel Office Clearance<br>
      Unit K4 B<br>
      3-7 Ferndale Lane<br>
      Harwick Vale<br>
      Eastbrook<br>
      ZZ9 4QX
    </address>
  </section>

</body>
</html>
```